Bright Harbor Works Buisness Cards

Provide a business card layout

Paul Wexford
PO Box 742
Ashcombe RI 02871
paul@thwexample.com

Industry/Entity Type

Business

Font styles to use
Serif

Colors
f04a50

```html
<!DOCTYPE html>
<html lang="en">
<head>
<meta charset="utf-8">
<title>Bright Harbor Works – Business Card</title>
<link rel="stylesheet" href="https://fonts.googleapis.com/css2?family=Crimson+Text:wght@400;600;700&display=swap">
<style>
  :root {
    --stage: #5b5b5b;
    --card-white: #ffffff;
    --coral: #f04a50;
    --amber: #eaa63a;
    --brick: #8f1a1e;
    --ink-light: #ffffff;
  }
  * { margin: 0; padding: 0; box-sizing: border-box; }
  html, body {
    width: 1200px;
    height: 900px;
    overflow: hidden;
    background: var(--stage);
    font-family: "Crimson Text", Georgia, serif;
  }
  .business-card {
    position: absolute;
    left: 100px;
    top: 165px;
    width: 1000px;
    height: 570px;
    background: var(--card-white);
    overflow: hidden;
    box-shadow: 0 18px 40px rgba(0,0,0,0.35);
  }
  .card-shapes {
    position: absolute;
    inset: 0;
    width: 100%;
    height: 100%;
  }
  .shape-coral { fill: var(--coral); }
  .shape-amber { fill: var(--amber); }

  .brand {
    position: absolute;
    left: 50px;
    top: 215px;
    width: 400px;
    display: flex;
    flex-direction: column;
    align-items: center;
    gap: 22px;
  }
  .brand-dot {
    width: 70px;
    height: 70px;
    border-radius: 50%;
    background: var(--amber);
  }
  .brand-name {
    color: var(--brick);
    font-weight: 700;
    font-size: 33px;
    letter-spacing: 1px;
    text-transform: uppercase;
    white-space: nowrap;
  }

  .contact {
    position: absolute;
    right: 52px;
    top: 345px;
    text-align: right;
    color: var(--ink-light);
  }
  .contact-name {
    font-size: 42px;
    font-weight: 400;
    line-height: 1.1;
    margin-bottom: 10px;
  }
  .contact-name .surname { font-weight: 600; }
  .contact-email {
    font-size: 24px;
    font-weight: 700;
    margin-bottom: 6px;
  }
  .contact-address {
    font-size: 23px;
    font-weight: 400;
  }
</style>
</head>
<body>
  <section class="business-card">
    <svg class="card-shapes" viewBox="0 0 1000 570" preserveAspectRatio="none" aria-hidden="true">
      <path class="shape-amber" d="M465 0 L575 0 L580 200 L535 335 C550 210 530 90 465 0 Z"/>
      <path class="shape-coral" d="M560 0 L1000 0 L1000 570 L420 570 C520 480 590 300 560 0 Z"/>
    </svg>

    <div class="brand">
      <span class="brand-dot"></span>
      <span class="brand-name">Bright Harbor Works</span>
    </div>

    <div class="contact">
      <p class="contact-name">Paul <span class="surname">Wexford</span></p>
      <p class="contact-email">paul@thwexample.com</p>
      <p class="contact-address">PO Box 742, Ashcombe RI 02871</p>
    </div>
  </section>
</body>
</html>
```